E-commerce Website needs category banner

What we need for our category banner is a clean, predominately black design that showcases the product we are trying to sell (currently only 1), and a few subtle gradients that follow the pattern set by previous designs.

An example will be provided to showcase what we want.

It needs to say:
Outdoor Motion Detection Lighting in large, clear font similar to the example provided.

Please ensure dimensions are as follows: 980x300

Target Market(s)

Senior citizens, businesses, homeowners, families, etc

Industry/Entity Type

Product

Font styles to use
Sans Serif

Requirements
Must have
• It needs to say:
Outdoor Motion Detection Lighting in large, clear font similar to the example provided
980x300 is the required size!
Should not have
• Too much going on- clean and simple please (no crazy fonts, logos, etc)

```html
<!DOCTYPE html>
<html lang="en">
<head>
<meta charset="utf-8">
<title>Outdoor Motion Detection Lighting</title>
<link rel="stylesheet" href="https://fonts.googleapis.com/css2?family=Open+Sans:wght@800&display=swap">
<style>
  :root {
    --bg-center: #565656;
    --bg-mid: #3a3a3a;
    --bg-edge: #242424;
    --headline: #ffffff;
    --product-light: rgba(226, 226, 222, 0.85);
    --product-mid: rgba(190, 190, 184, 0.55);
    --product-fade: rgba(120, 120, 116, 0);
  }
  html, body {
    margin: 0;
    padding: 0;
    width: 1200px;
    height: 469px;
    overflow: hidden;
    background: var(--bg-edge);
  }
  .category-banner {
    position: relative;
    width: 1200px;
    height: 469px;
    overflow: hidden;
    background:
      radial-gradient(ellipse 65% 80% at 55% 35%, var(--bg-center) 0%, var(--bg-mid) 50%, var(--bg-edge) 100%);
  }
  .headline {
    position: absolute;
    left: 97px;
    top: 45px;
    margin: 0;
    font-family: "Open Sans", Arial, sans-serif;
    font-weight: 800;
    font-size: 74px;
    line-height: 98px;
    letter-spacing: 0.5px;
    color: var(--headline);
    text-transform: uppercase;
    white-space: nowrap;
  }
  .headline span {
    display: block;
  }
  .product-shot {
    position: absolute;
    left: 560px;
    top: 50px;
    width: 630px;
    height: 390px;
    background:
      radial-gradient(ellipse 50% 50% at 55% 50%, var(--product-light) 0%, var(--product-mid) 55%, var(--product-fade) 100%);
  }
</style>
</head>
<body>
  <main class="category-banner">
    <h1 class="headline">
      <span>Outdoor</span>
      <span>Motion</span>
      <span>Detection</span>
      <span>Lighting</span>
    </h1>
    <div class="product-shot" role="img" aria-label="Three white battery-powered outdoor motion sensor spotlights of increasing size, each with twin LED lamps above a motion sensor dome on a swivel wall mount"></div>
  </main>
</body>
</html>
```